LA Billboard Project for Brisk Lending

We are running three different billboards around LA, and we need someone to take the mock-ups I've created and bring this campaign to life. Whatever wording is on the mock-ups should stay the same in the ads you create, but feel free to get creative with layout and style. I've attached our mock-ups, our style guide, our logo, and the necessary specs for the billboards. If you have any questions, feel free to reach out!

```html
<!DOCTYPE html>
<html lang="en">
<head>
<meta charset="utf-8">
<title>Brisk Lending – Billboard Campaign</title>
<link rel="stylesheet" href="https://fonts.googleapis.com/css2?family=Cinzel:wght@600&family=Lexend:wght@400;500;700;800&display=swap">
<style>
  :root {
    --page-grey: #a9a9a9;
    --navy: #0d2142;
    --navy-light: #143058;
    --teal: #16bcd4;
    --sky: #7fd9ea;
    --yellow: #f9dc1c;
    --yellow-bright: #fff200;
    --white: #ffffff;
  }
  * { margin: 0; padding: 0; box-sizing: border-box; }
  html, body { width: 800px; height: 1200px; overflow: hidden; }
  body {
    background: var(--page-grey);
    position: relative;
    font-family: "Lexend", sans-serif;
  }
  .billboard {
    position: absolute;
    left: 53px;
    width: 695px;
    height: 321px;
    background: var(--navy);
    overflow: hidden;
  }
  .billboard--facts { top: 67px; }
  .billboard--strategy { top: 440px; background: linear-gradient(115deg, #0b1d3c 0%, #10284d 45%, #0c2142 100%); }
  .billboard--traffic { top: 812px; }
  .billboard__art { position: absolute; inset: 0; width: 695px; height: 321px; }
  .brand {
    position: absolute;
    left: 42px;
    top: 34px;
    display: flex;
    align-items: center;
    gap: 8px;
    color: var(--teal);
    font-weight: 700;
    font-size: 28px;
    letter-spacing: -0.5px;
  }
  .brand__square { width: 14px; height: 14px; background: var(--teal); }
  .headline {
    position: absolute;
    left: 42px;
    font-weight: 800;
    text-transform: uppercase;
    line-height: 1;
  }
  .headline--know { top: 130px; font-size: 31px; color: var(--yellow); letter-spacing: 1px; }
  .headline-rule { position: absolute; left: 42px; top: 165px; width: 58px; height: 3px; background: var(--teal); }
  .fact {
    position: absolute;
    left: 42px;
    top: 189px;
    width: 270px;
    font-size: 12.5px;
    line-height: 18.5px;
    color: var(--white);
  }
  .fact em { font-style: normal; color: var(--yellow); }
  .question { position: absolute; left: 42px; top: 118px; line-height: 1; }
  .question__lead { display: block; font-family: "Cinzel", serif; font-size: 29px; color: var(--white); }
  .question__key { display: block; font-weight: 800; font-size: 47px; color: var(--yellow); margin-top: 6px; }
  .question__end { display: block; font-weight: 800; font-size: 37px; color: var(--yellow); margin-top: 3px; }
  .slogan { position: absolute; left: 42px; top: 133px; text-transform: uppercase; font-weight: 800; line-height: 1; }
  .slogan__setup { display: block; color: var(--white); font-size: 25px; }
  .slogan__payoff { display: block; color: var(--yellow); font-size: 27px; font-weight: 700; line-height: 30px; margin-top: 20px; }
  .web {
    position: absolute;
    left: 42px;
    top: 277px;
    font-size: 15px;
    font-weight: 700;
    color: var(--teal);
    letter-spacing: 0.5px;
  }
  .base-bar { position: absolute; left: 42px; bottom: 0; width: 158px; height: 5px; background: var(--yellow); }
</style>
</head>
<body>

<section class="billboard billboard--facts">
  <svg class="billboard__art" viewBox="0 0 695 321">
    <defs>
      <linearGradient id="laptopTones" x1="0" y1="0" x2="1" y2="1">
        <stop offset="0" stop-color="#d9d3cc"/>
        <stop offset="0.5" stop-color="#eeeeee"/>
        <stop offset="1" stop-color="#7b6656"/>
      </linearGradient>
    </defs>
    <path d="M346 0 H430 A265 200 0 0 1 695 200 V321 H346 Z" fill="var(--teal)"/>
    <polygon points="411,105 520,50 629,105 629,321 411,321" fill="url(#laptopTones)" role="img" aria-label="Photo of a hand typing on a laptop showing a mortgage page"/>
  </svg>
  <div class="brand"><span class="brand__square"></span>Brisk Lending</div>
  <h2 class="headline headline--know">Did You Know</h2>
  <div class="headline-rule"></div>
  <p class="fact">That Same-Sex Borrowers are <em>73%</em> More Likely to be Denied When Applying for a <em>Mortgage Loan?</em></p>
  <div class="web">BRISKLENDING.COM/LGBTQ</div>
  <div class="base-bar"></div>
</section>

<section class="billboard billboard--strategy">
  <svg class="billboard__art" viewBox="0 0 695 321">
    <defs>
      <linearGradient id="houseTones" x1="0" y1="0" x2="1" y2="1">
        <stop offset="0" stop-color="#f1f1f1"/>
        <stop offset="0.6" stop-color="#b9b4ae"/>
        <stop offset="1" stop-color="#4e5358"/>
      </linearGradient>
    </defs>
    <polygon points="150,0 260,0 90,321 -20,321" fill="var(--navy-light)" opacity="0.45"/>
    <polygon points="560,0 640,0 520,321 440,321" fill="var(--navy-light)" opacity="0.45"/>
    <rect x="394" y="18" width="127" height="110" fill="var(--sky)"/>
    <rect x="485" y="55" width="128" height="113" fill="var(--teal)"/>
    <rect x="373" y="267" width="169" height="35" fill="var(--yellow-bright)"/>
    <path d="M393 80 H662 V250 H695 V321 H600 V260 H393 Z" fill="url(#houseTones)" role="img" aria-label="Photo of a hand holding a model house with clouds"/>
  </svg>
  <div class="brand"><span class="brand__square"></span>Brisk Lending</div>
  <h2 class="question">
    <span class="question__lead">WHAT’S YOUR</span>
    <span class="question__key">MORTGAGE</span>
    <span class="question__end">STRATEGY?</span>
  </h2>
  <div class="web">BRISKLENDING.COM</div>
  <div class="base-bar" style="width:145px"></div>
</section>

<section class="billboard billboard--traffic">
  <svg class="billboard__art" viewBox="0 0 695 321">
    <defs>
      <linearGradient id="trafficTones" x1="0" y1="0" x2="0" y2="1">
        <stop offset="0" stop-color="#2a1d18"/>
        <stop offset="0.45" stop-color="#8a4a2a"/>
        <stop offset="1" stop-color="#5a2a22"/>
      </linearGradient>
    </defs>
    <polygon points="355,0 467,0 431,100" fill="var(--yellow)"/>
    <polygon points="467,0 474,0 386,321 379,321" fill="var(--teal)"/>
    <polygon points="474,0 695,0 695,321 386,321" fill="url(#trafficTones)" role="img" aria-label="Night photo of a city highway in heavy traffic"/>
  </svg>
  <div class="brand"><span class="brand__square"></span>Brisk Lending</div>
  <h2 class="slogan">
    <span class="slogan__setup">Traffic is a mess.</span>
    <span class="slogan__payoff">Your mortgage<br>doesn’t have to be.</span>
  </h2>
  <div class="web">BRISKLENDING.COM</div>
  <div class="base-bar"></div>
</section>

</body>
</html>
```